Business card design needed

I need a business card for my new Food & Lifestyle Coaching business - "Bloomvale Food & Lifestlye Coaching"

i already have a logo and would like to have that incorporated into the business card, obviously.

i would like a design that says "fresh" and "funky" - my target market is female, aged 20-45 so i want something that will stand out to them when they see it.

My "Company Colour" is Apple Green
Updates

Thankyou to everyone who has submitted a design for my project. At this stage i have quite a large number of designs to chose from and with only a short time until my project closes i am focusing now on chosing from those i have already shortlisted so am unfortunately not considering any new desings.

Thankyou again for your interest in my project.

Target Market(s)

Female, Health Conscious (or looking to improve their health/lifestyle), aged between 20-45

Industry/Entity Type

Business

Contact Information for Business Card

Tamsin Corley
Ph: 0417382946
Email: eatwell@marovex.com

Requirements
Must have
• Must include my existing Logo
Nice to have
• Would be nice to incoirporate and appointment card on the back

```html
<!DOCTYPE html>
<html lang="en">
<head>
<meta charset="utf-8">
<title>Bloomvale Food &amp; Lifestlye Coaching – Business &amp; Appointment Card</title>
<link rel="stylesheet" href="https://fonts.googleapis.com/css2?family=Quicksand:wght@500;600;700&family=Parisienne&family=Dancing+Script:wght@500&display=swap">
<style>
  :root{
    --apple-green:#8cc63f;
    --leaf-light:#b5dc83;
    --ink:#2b2b2b;
    --paper:#ffffff;
    --stage:#ecebe6;
    --dots:#555555;
    --sunday:#e8342b;
  }
  *{box-sizing:border-box;margin:0;padding:0}
  html,body{width:1200px;height:867px;overflow:hidden;background:var(--stage)}
  .stage{position:relative;width:1200px;height:867px}
  .card{position:absolute;top:274px;width:520px;height:318px;background:var(--paper);
        border-radius:14px;overflow:hidden;box-shadow:0 6px 18px rgba(0,0,0,.18)}
  .card--front{left:60px}
  .card--back{left:620px}

  /* brand lockup */
  .brand{display:flex;flex-direction:column;align-items:center;font-family:"Quicksand",sans-serif;color:var(--ink)}
  .brand__row{display:flex;align-items:center;gap:10px}
  .brand__dot{width:22px;height:22px;border-radius:50%;background:var(--apple-green)}
  .brand__name{font-weight:600;font-size:40px;line-height:1;letter-spacing:.5px}
  .brand__tagline{font-weight:600;font-size:11px;margin-top:4px}

  /* front */
  .front__top{height:142px;display:flex;align-items:center;justify-content:center}
  .front__band{position:absolute;left:0;right:0;bottom:0;height:176px;background:var(--apple-green);
               display:flex;align-items:center;color:var(--paper)}
  .front__name{width:250px;text-align:center;font-family:"Parisienne",cursive;font-size:34px;color:var(--ink)}
  .front__divider{width:0;height:100px;border-left:2px dotted var(--ink)}
  .front__contact{flex:1;padding-left:34px;font-family:"Dancing Script",cursive}
  .front__phone{font-size:26px;letter-spacing:1.5px}
  .front__email{font-size:17px;margin-top:6px}

  /* back */
  .back__pattern{position:absolute;left:0;top:0;bottom:0;width:196px;
                 background:linear-gradient(135deg,var(--apple-green),#9fd159 55%,var(--apple-green))}
  .back__form{position:absolute;left:196px;right:0;top:0;bottom:0;padding:24px 26px 0 26px;
              font-family:"Quicksand",sans-serif}
  .back__form .brand__name{font-size:32px}
  .back__form .brand__dot{width:18px;height:18px}
  .back__form .brand__tagline{font-size:9px}
  .dotline{border-bottom:2px dotted var(--dots)}
  .back__client{margin-top:30px}
  .back__label{color:var(--apple-green);font-weight:600;font-size:15px;text-align:center;margin-top:10px}
  .days{display:flex;justify-content:space-between;margin-top:14px;padding:0 4px}
  .day{display:flex;flex-direction:column;align-items:center;gap:6px;font-weight:700;font-size:13px;color:var(--apple-green)}
  .day__box{width:22px;height:22px;border:1.5px solid #666;border-radius:4px}
  .day--sunday{color:var(--sunday)}
  .when{display:flex;align-items:flex-end;gap:8px;margin-top:22px}
  .when__field{flex:1;text-align:center}
  .when__field .dotline{height:20px}
  .when__caption{color:var(--apple-green);font-weight:600;font-size:14px;margin-top:4px}
  .when__at{font-weight:700;font-size:13px;color:#444;padding-bottom:24px}
  .when__ampm{font-weight:700;font-size:13px;color:#444;line-height:1.2;padding-bottom:20px}
</style>
</head>
<body>
<main class="stage">

  <section class="card card--front" aria-label="Business card front">
    <div class="front__top">
      <div class="brand">
        <div class="brand__row"><span class="brand__dot"></span><span class="brand__name">Bloomvale</span></div>
        <span class="brand__tagline">Food &amp; Lifestlye Coaching</span>
      </div>
    </div>
    <div class="front__band">
      <p class="front__name">Tamsin Corley</p>
      <span class="front__divider"></span>
      <div class="front__contact">
        <p class="front__phone">0417 382 946</p>
        <p class="front__email">eatwell@marovex.com</p>
      </div>
    </div>
  </section>

  <section class="card card--back" aria-label="Appointment card back">
    <div class="back__pattern" role="img" aria-label="Repeating pattern of light green leaves on apple green"></div>
    <div class="back__form">
      <div class="brand">
        <div class="brand__row"><span class="brand__dot"></span><span class="brand__name">Bloomvale</span></div>
        <span class="brand__tagline">Food &amp; Lifestlye Coaching</span>
      </div>
      <div class="dotline back__client"></div>
      <p class="back__label">Has an appointment on</p>
      <div class="days">
        <div class="day"><span class="day__box"></span>M</div>
        <div class="day"><span class="day__box"></span>T</div>
        <div class="day"><span class="day__box"></span>W</div>
        <div class="day"><span class="day__box"></span>T</div>
        <div class="day"><span class="day__box"></span>F</div>
        <div class="day"><span class="day__box"></span>S</div>
        <div class="day day--sunday"><span class="day__box"></span>S</div>
      </div>
      <div class="when">
        <div class="when__field"><div class="dotline"></div><p class="when__caption">Date</p></div>
        <span class="when__at">AT</span>
        <div class="when__field"><div class="dotline"></div><p class="when__caption">Time</p></div>
        <span class="when__ampm">am<br>pm</span>
      </div>
    </div>
  </section>

</main>
</body>
</html>
```